Business Card Upgrade

I have designed our business card using our new logo. I think it needs imporovements. We used to have two cards for our business. One card was for our software business, and the other was for our consulting business. We are now in the process of combining our websites, marketing, name, and a new logo.

Our goal is to have a really sharp professional logo. One reason I designed the card the way I did was that our Titles are sometimes long, and by separating the person's name and title, it shows up very well and the title can be adjusted no matter how long it is. Sometimes the title can be 4 or 5 words or more.

We really like our logo on black as it shows up very nice. Our PMS colors are as follows: 368C and 459C.

The Designer that will be working with us will need to deliver the following:

The front and back of the Business Card Design will need to be delivered in a high quality JPEG, and
The front and back of the Business Card Design in Illustrator Format .ai
Any fonts will need to be sent to us if they are not standard and are required to open the Illustrator file correctly.

To help us get a good idea of the card with a title, please use the title: " Director of Software Development "

NOTE: The chosen designer will be selected to design our new letterhead within 2 weeks from the closing of this contest.

To help us make sure the card design works with longer titles, please use the followign job title on the card:  

"Director of Software and Product Development"

 

ALL DESIGNERS:

1. I appreciate the different angles you are showing the cards, but please be sure and always show the direct view, so I can see the layout and what the person I hand the card will see.

2. Please do not use white.  Please use off white as I don't care for white cards and they get dirty easy and do not represent the designs well.

Dear Designers,

Please provide samples straight one as a viewer of the card will see.  Some of the angles that are presented make it impossible to tell how everything fits, and sometimes even makes areas look skewed. So, please provide a straight sample view.

Pinnacle 400 company executives such as Vice Presidents, and Directors

Software

• Professional looking Card.

Our customers are Directors, Vice Presidents, and Presidents of companies as large as Pinnacle 400 companies. The card needs to get attention wile still looking professional.

Delivery of the finished product in Illustrator Format with any fonts needed to edit the text or open the file.

The card will be a heavy stock with a soft touch coating for that silk feel.

```html
<!DOCTYPE html>
<html lang="en">
<head>
<meta charset="utf-8">
<title>Meridian Trade Zone Corporation – Business Card</title>
<link rel="stylesheet" href="https://fonts.googleapis.com/css2?family=EB+Garamond:wght@400;500&display=swap">
<style>
  :root {
    --ink: #050606;
    --green: #62ad47;
    --green-deep: #0f2a17;
    --green-line: #1f4a27;
    --gold: #e6d592;
    --gold-soft: #efe2a6;
    --paper-gap: #ffffff;
    --trim-red: #e03a2f;
  }
  * { box-sizing: border-box; margin: 0; padding: 0; }
  html, body {
    width: 1065px;
    height: 1200px;
    overflow: hidden;
    background: var(--paper-gap);
  }
  .sheet {
    position: relative;
    width: 1065px;
    height: 1200px;
    font-family: "EB Garamond", Garamond, serif;
  }

  /* Front of card */
  .card-front {
    position: absolute;
    left: 0; top: 3px;
    width: 1065px; height: 592px;
    background: var(--ink);
    overflow: hidden;
  }
  .front-backdrop {
    position: absolute; inset: 0;
    background:
      radial-gradient(ellipse 70% 55% at 50% 100%, rgba(31,74,39,0.55), transparent 70%),
      radial-gradient(ellipse 90% 40% at 50% 0%, rgba(15,42,23,0.9), transparent 75%),
      var(--ink);
  }
  .brand-name {
    position: absolute;
    left: 0; right: 0; top: 205px;
    text-align: center;
    color: var(--green);
    font-weight: 500;
    font-size: 76px;
    line-height: 1.05;
    letter-spacing: 2px;
  }

  /* Trim between sides */
  .trim-line {
    position: absolute;
    left: 0; top: 596px;
    width: 1048px; height: 2px;
    background: var(--trim-red);
  }

  /* Back of card */
  .card-back {
    position: absolute;
    left: 0; top: 605px;
    width: 1065px; height: 595px;
    background: var(--ink);
    overflow: hidden;
  }
  .back-edge {
    position: absolute; top: 0; bottom: 0;
    width: 16px;
    background: linear-gradient(180deg, var(--green-deep), #0a1a0e 60%, var(--green-deep));
  }
  .back-edge.left { left: 0; }
  .back-edge.right { right: 0; }

  .job-title {
    position: absolute;
    left: 0; right: 0; top: 60px;
    text-align: center;
    color: var(--green);
    font-size: 41px;
    font-weight: 400;
  }
  .glow-rule {
    position: absolute;
    left: 16px; right: 16px; top: 170px;
    height: 66px;
  }
  .person {
    position: absolute;
    left: 355px; top: 278px;
  }
  .person-name {
    color: var(--green);
    font-size: 42px;
    line-height: 1.1;
  }
  .person-role {
    color: var(--gold);
    font-size: 26px;
    line-height: 1.2;
  }
  .contact {
    position: absolute;
    left: 38px; top: 430px;
    font-size: 34px;
    line-height: 42px;
    color: var(--gold);
  }
  .contact .web { color: var(--green); }
  .address {
    position: absolute;
    left: 673px; top: 428px;
    font-size: 34px;
    line-height: 42px;
    color: var(--gold);
  }
</style>
</head>
<body>
<main class="sheet">

  <section class="card-front" aria-label="Card front">
    <div class="front-backdrop" role="img" aria-label="Dark background with fine green radiating lines"></div>
    <h1 class="brand-name">Meridian Trade Zone<br>Corporation</h1>
  </section>

  <div class="trim-line"></div>

  <section class="card-back" aria-label="Card back">
    <div class="back-edge left"></div>
    <div class="back-edge right"></div>

    <p class="job-title">Director of Software Development</p>

    <svg class="glow-rule" viewBox="0 0 1033 66" preserveAspectRatio="none" aria-hidden="true">
      <defs>
        <linearGradient id="glowBand" x1="0" y1="0" x2="0" y2="1">
          <stop offset="0" stop-color="#e6d592" stop-opacity="0"/>
          <stop offset="0.5" stop-color="#e6d592" stop-opacity="0.35"/>
          <stop offset="1" stop-color="#e6d592" stop-opacity="0"/>
        </linearGradient>
      </defs>
      <rect x="0" y="14" width="1033" height="38" fill="url(#glowBand)"/>
      <rect x="0" y="31" width="1033" height="4" fill="#efe2a6"/>
    </svg>

    <div class="person">
      <p class="person-name">Dana Whitlow</p>
      <p class="person-role">President</p>
    </div>

    <div class="contact">
      <p>Direct Phone: (251) 555-0148</p>
      <p>Email: dwhitlow@meridiantz.com</p>
      <p class="web">www.meridiantz.com</p>
    </div>

    <address class="address" style="font-style:normal">
      <p>418 Harbor View Lane</p>
      <p>Bayport, AL 36690</p>
    </address>
  </section>

</main>
</body>
</html>
```